HVAC company business card design

We need a business card design for a HVAC company. The design must look professional. Both sides will be used. The total data to be on the business card is
Name
Position
Email
Direct Phone/Moile Phone
Company Contacts /Address, Phone, Fax, web)
All data will be submit once the design is confirmed. For generic purposes use;
Emre Toksoy
Managing Director
+902324815263 (Mobile)
4712 Sokak No: 9 KBSE Yenikent IZMIR TURKEY
Tel: +902324815263 Fax : +902324815269
www.luvon.com.tr

Target Market(s)

HVAC

Industry/Entity Type

Business

Contact Information for Business Card

The total data to be on the business card is
Name
Position
Email
Direct Phone/Moile Phone
Emre Toksoy
Managing Director
+902324815263 (Mobile)
www.luvon.com.tr
The BC will use both sides of the card. The front will include the full logo and the details for the business card holder. The business card can be divided into vertical/horizontal or to a special shape. The common data like the company address/phone/fax should be indicated elsewehere. The back can contain some part or the whole logo and must contain the web address.

Font styles to use
Serif
Sans Serif

Colors
0355a3
cfdfed

Requirements
Should not have
• Please be careful with the fonts, it shouldnt be too small or too big and must not interfere with the logo fonts. If you need to use a curvy shape please do not use as the logo is already curvy or use the curves from the logo (if it looks good, otherwise forget it)
• We are not in favor of pictograms, only if they are perfect use them.

```html
<!DOCTYPE html>
<html lang="en">
<head>
<meta charset="utf-8">
<title>Luvon business card</title>
<link href="https://fonts.googleapis.com/css2?family=Lato:wght@400;700&display=swap" rel="stylesheet">
<style>
  :root {
    --backdrop: #2a2a2c;
    --card: #fbfcfd;
    --brand-blue: #2b6cc4;
    --brand-navy: #323c58;
    --ink-grey: #6d7480;
    --name-blue: #6f9bd6;
    --contact-blue: #3f74c6;
    --pale-blue: #cfdfed;
  }
  * { margin: 0; padding: 0; box-sizing: border-box; }
  html, body { width: 1200px; height: 997px; overflow: hidden; }
  body {
    background: var(--backdrop);
    font-family: "Lato", Arial, sans-serif;
    position: relative;
  }
  .card {
    position: absolute;
    left: 250px;
    width: 700px;
    height: 400px;
    background: var(--card);
    overflow: hidden;
    box-shadow: 0 10px 30px rgba(0,0,0,.45);
  }
  .card--front { top: 58px; }
  .card--back { top: 539px; }

  /* Front side */
  .front__halo {
    position: absolute;
    right: -40px; top: -120px;
    width: 300px; height: 300px;
    border-radius: 50%;
    background: var(--pale-blue);
    opacity: .35;
  }
  .holder { position: absolute; left: 44px; top: 60px; }
  .holder__name { font-size: 19px; color: var(--name-blue); font-weight: 400; }
  .holder__role { font-size: 12px; color: var(--ink-grey); margin-top: 2px; letter-spacing: .3px; }

  .contact-list { position: absolute; left: 78px; top: 252px; list-style: none; }
  .contact-list li { font-size: 14px; color: var(--contact-blue); line-height: 19px; height: 19px; }

  .icon-strip {
    position: absolute; left: 32px; top: 250px;
    width: 36px; height: 150px;
    background: var(--brand-blue);
  }
  .icon-strip svg { display: block; margin: 6px auto 0; }

  .address-band {
    position: absolute; left: 0; bottom: 22px;
    width: 100%; height: 26px;
    background: var(--brand-blue);
    color: #fff; font-size: 13px; font-weight: 700;
    text-align: right; padding-right: 40px; line-height: 26px;
  }

  .brand { position: absolute; display: flex; align-items: center; }
  .brand__dot { border-radius: 50%; background: var(--brand-blue); }
  .brand__name { color: var(--brand-navy); font-weight: 700; letter-spacing: 2px; }
  .card--front .brand { right: 40px; top: 255px; gap: 14px; }
  .card--front .brand__dot { width: 52px; height: 52px; }
  .card--front .brand__name { font-size: 46px; }

  /* Back side */
  .card--back .brand { left: 110px; top: 90px; gap: 26px; }
  .card--back .brand__dot { width: 120px; height: 120px; }
  .card--back .brand__name { font-size: 96px; letter-spacing: 4px; }
  .web-band {
    position: absolute; left: 0; top: 262px;
    width: 100%; height: 20px;
    background: var(--brand-blue);
  }
  .web-band--lower { top: 330px; height: 42px; }
  .web-band__url {
    color: #fff; font-size: 15px; font-weight: 700; letter-spacing: 6px;
    text-align: center; line-height: 42px;
  }
</style>
</head>
<body>

<section class="card card--front" aria-label="Business card front">
  <div class="front__halo"></div>

  <div class="holder">
    <p class="holder__name">Emre Toksoy</p>
    <p class="holder__role">Managing Director</p>
  </div>

  <div class="icon-strip">
    <svg width="14" height="14" viewBox="0 0 14 14"><rect x="3" y="1" width="8" height="12" rx="1.5" fill="none" stroke="#fff" stroke-width="1.4"/></svg>
    <svg width="14" height="14" viewBox="0 0 14 14"><path d="M2 9c0-4 10-4 10 0v2H2z" fill="#fff"/><rect x="4" y="3" width="6" height="3" fill="#fff"/></svg>
    <svg width="14" height="14" viewBox="0 0 14 14"><rect x="1" y="5" width="12" height="7" fill="#fff"/><rect x="4" y="2" width="6" height="3" fill="none" stroke="#fff"/></svg>
    <svg width="14" height="14" viewBox="0 0 14 14"><rect x="1" y="3" width="12" height="8" fill="none" stroke="#fff" stroke-width="1.4"/><path d="M1 3l6 5 6-5" fill="none" stroke="#fff" stroke-width="1.2"/></svg>
  </div>

  <ul class="contact-list">
    <li>+902324815263</li>
    <li>+902324815263</li>
    <li>+902324815269</li>
    <li>enquiries@luvon.com.tr</li>
  </ul>

  <div class="brand">
    <span class="brand__dot"></span>
    <span class="brand__name">LUVON</span>
  </div>

  <div class="address-band">4712 Sokak No: 9 KBSE Yenikent IZMIR TURKEY</div>
</section>

<section class="card card--back" aria-label="Business card back">
  <div class="brand">
    <span class="brand__dot"></span>
    <span class="brand__name">LUVON</span>
  </div>
  <div class="web-band"></div>
  <div class="web-band web-band--lower">
    <p class="web-band__url">www.luvon.com.tr</p>
  </div>
</section>

</body>
</html>
```